Cartwell site design for e-commerce brand

I need a cartwell website for my smoking accessory brand. The name of the brand is called "RiverMoss Smoking Supplies" i need the website to have a "Sleek And modern Design" preferable with a "Black/ white Colour Scheme" . Ideally would like the site to match the packaging design of my products (see image below) if not possible will be open to other designs.
To Add need the cartwell store to be "Integrated With Pictaro and Friendvale" (@rivermosssmokingsupplies . In addition to Friendvale “rivermoss smoking supplies”) ...
Furthermore i need to be able to "Easily to upload future products" (Current only have 7 with one I’m looking to launch soon ). I will also need to be "Able to capture emails to use for email marketing in the future as the brand grows
I’m currently selling my products on quellmart, see links below;
https://www.quellmart.example/dp/X71P2KD9QA?ref=shop_item
https://www.quellmart.example/dp/X74M8NW3TB?ref=shop_item
https://www.quellmart.example/dp/X74M9RE6UC?ref=shop_item
https://www.quellmart.example/dp/X62T51HJVD?ref=shop_item
https://www.quellmart.example/dp/X62T51ZPWE?ref=shop_item
https://www.quellmart.example/dp/X62T517QXF?ref=shop_item
https://www.quellmart.example/dp/X58KWB4NYG?ref=shop_item
Target Market(s)
Cannabis / weed Smokers
Look and feel
Each slider illustrates characteristics of the customer's brand and the style your logo design should communicate.

```html
<!DOCTYPE html>
<html lang="en">
<head>
<meta charset="utf-8">
<title>RiverMoss Smoking Supplies</title>
<link href="https://fonts.googleapis.com/css2?family=Jost:wght@400;500;600;700;800&display=swap" rel="stylesheet">
<style>
:root{
  --ink:#111111;
  --nav:#1c1c1c;
  --white:#ffffff;
  --mist:#e7e8ec;
  --grey:#6a6a6a;
  --text:#222222;
  --pill:#7c8191;
  --star:#f2c218;
  --line:#3a3a3a;
}
*{box-sizing:border-box;margin:0;padding:0}
html,body{width:1200px;height:4342px;overflow:hidden}
body{font-family:'Jost',sans-serif;color:var(--text);background:var(--white);position:relative}
.abs{position:absolute}
.photo{position:absolute}
/* top */
.topbar{left:0;top:0;width:1200px;height:42px;background:var(--ink);color:var(--white);font-size:13px;font-weight:500;display:flex;align-items:center;justify-content:center}
.navbar{left:0;top:42px;width:1200px;height:68px;background:var(--nav);display:flex;align-items:center;padding-left:100px}
.brand{color:var(--white);font-weight:800;font-size:30px;letter-spacing:.5px;line-height:1;text-align:center}
.brand small{display:block;font-size:8px;letter-spacing:3px;font-weight:700;margin-top:3px}
.menu{display:flex;gap:37px;margin-left:50px;list-style:none}
.menu li{color:var(--white);font-size:15px;font-weight:500}
.nav-icons{display:flex;gap:16px;margin-left:36px}
/* hero */
.hero{left:0;top:110px;width:1200px;height:588px;background:radial-gradient(ellipse at 75% 45%,#5c5c5c 0%,#2c2c2c 45%,#151515 100%)}
.hero-copy{left:100px;top:182px;width:470px;color:var(--white)}
.hero-title{font-size:42px;font-weight:800;text-transform:uppercase;letter-spacing:-.5px;line-height:1}
.hero-text{font-size:13px;line-height:25px;margin-top:18px}
.btn-outline{display:inline-block;margin-top:24px;border:1.5px solid var(--white);color:var(--white);font-size:14px;font-weight:600;padding:13px 28px}
.welcome{left:0;top:698px;width:1200px;height:52px;background:var(--mist);font-size:16px;display:flex;align-items:center;justify-content:center}
/* intro */
.intro{left:0;width:1200px;text-align:center}
.intro h2{font-size:18px;font-weight:600}
.intro p{font-size:12.5px;color:var(--grey);line-height:24px;width:860px;margin:14px auto 0}
/* products */
.products{left:100px;top:935px;width:1000px;display:flex;justify-content:space-between}
.card{width:240px;text-align:center}
.card .photo{position:relative;height:215px;margin:0 auto;width:210px;background:radial-gradient(ellipse at 50% 60%,#2a2a2a 0%,#3c3c3c 50%,#ffffff 72%)}
.card h3{font-size:12px;font-weight:500;margin-top:30px}
.rating{display:flex;justify-content:center;align-items:center;gap:6px;font-size:12px;color:var(--grey);margin-top:8px}
.price{font-size:12px;color:var(--grey);margin-top:8px}
.btn-dark{background:var(--ink);color:var(--white);font-size:14px;font-weight:600;display:flex;align-items:center;justify-content:center;border-radius:3px}
/* stories */
.stories{left:99px;top:1395px;width:1002px;display:flex;justify-content:space-between}
.story{width:321px;text-align:center}
.story .photo{position:relative;height:368px;background:linear-gradient(160deg,#8a8a8a,#2e2e2e 60%,#cfcfcf)}
.story h3{font-size:15px;font-weight:600;margin-top:18px;letter-spacing:.3px}
.story p{font-size:11px;color:var(--grey);line-height:22px;margin-top:8px}
/* promo */
.promo{left:0;top:1950px;width:1200px;height:52px;background:var(--mist);display:flex;align-items:center;justify-content:center;font-size:15px;gap:6px}
.promo b{font-weight:700}
.promo .btn-small{margin-left:14px;border:1px solid #999;background:var(--white);font-size:9px;font-weight:700;padding:8px 20px;border-radius:2px}
.feature-photo{left:0;top:2002px;width:1200px;height:684px;background:linear-gradient(90deg,#a9a9a9 0%,#d2d2d2 45%,#b8b8b8 70%,#9a9a9a 100%)}
.feature{left:89px;width:412px;height:110px;display:flex;align-items:center}
.feature .dot{width:110px;height:110px;border-radius:50%;background:radial-gradient(circle,#111 55%,#3b3b3b 60%,#7c8191 63%);flex:none;position:relative;z-index:2}
.feature .pill{margin-left:-54px;padding-left:74px;height:84px;width:356px;background:var(--pill);border-radius:0 16px 16px 0;color:var(--white);display:flex;flex-direction:column;justify-content:center}
.feature h4{font-size:20px;font-weight:600}
.feature p{font-size:11px;line-height:18px}
/* gallery */
.duo{top:2900px;height:467px}
.duo-left{left:0;width:595px;background:linear-gradient(135deg,#3a3a3a,#1c1c1c 55%,#6f6f6f)}
.duo-right{left:603px;width:597px;background:linear-gradient(200deg,#6a6a6a,#2a2a2a 50%,#8c8c8c)}
.offer{top:3437px;width:280px}
.offer h3{font-size:15px;font-weight:600;line-height:23px}
.offer p{font-size:11px;color:var(--grey);line-height:19px;margin-top:12px}
.offer .btn-dark{width:118px;height:38px;font-size:12px;margin-top:18px}
.offer-photo{top:3437px;height:220px;background:radial-gradient(ellipse at 50% 55%,#1a1a1a 0%,#333 45%,#ffffff 72%)}
/* signup */
.signup{left:0;top:3744px;width:1200px;height:283px;background:var(--mist);text-align:center}
.signup h2{font-size:26px;font-weight:500;margin-top:80px;letter-spacing:.5px}
.signup p{font-size:15px;margin-top:8px}
.signup-form{display:flex;width:500px;height:47px;margin:22px auto 0;border:1px solid #9a9a9a;background:var(--white)}
.signup-form span{flex:1;text-align:left;padding-left:22px;font-size:14px;color:var(--grey);display:flex;align-items:center}
.signup-form b{width:104px;background:var(--ink);color:var(--white);font-size:14px;font-weight:600;display:flex;align-items:center;justify-content:center}
/* footer */
.footer{left:0;top:4027px;width:1200px;height:315px;background:var(--ink);color:var(--white)}
.footer .brand{position:absolute;left:88px;top:68px;width:193px;font-size:36px}
.socials{position:absolute;left:114px;top:166px;display:flex;gap:8px}
.socials i{display:block;width:34px;height:34px;border:1.5px solid var(--white);border-radius:50%}
.fcol{position:absolute;top:70px}
.fcol h5{font-size:14px;font-weight:600;letter-spacing:.5px}
.fcol ul{list-style:none;margin-top:10px}
.fcol li{font-size:14px;line-height:26px}
.fcol p{font-size:14px;line-height:26px;margin-top:8px;width:280px}
.fmail{margin-top:10px;width:278px;height:42px;background:#1f1f1f;display:flex;align-items:center;justify-content:space-between;padding:0 14px;font-size:13px}
.frule{position:absolute;left:88px;top:253px;width:1012px;height:1px;background:var(--line)}
.copy{position:absolute;left:88px;top:272px;font-size:13px}
.cards{position:absolute;left:912px;top:268px;display:flex;gap:4px}
.cards i{display:block;width:34px;height:22px;background:#d9d9d9;border-radius:2px}
</style>
</head>
<body>

<div class="abs topbar">FREE DELIVERY On orders Over $20</div>

<header class="abs navbar">
  <div class="brand">RiverMoss<small>SMOKING SUPPLIES</small></div>
  <ul class="menu">
    <li>HOME</li><li>PRODUCTS</li><li>ORDER TRACKING</li><li>ABOUT</li><li>REVIEW</li><li>SUPPORT</li><li>FAQ</li>
  </ul>
  <div class="nav-icons">
    <svg width="22" height="22" viewBox="0 0 22 22" fill="none" stroke="#fff" stroke-width="1.5"><circle cx="11" cy="7" r="4.5"/><path d="M2.5 21c1-5 4.5-7 8.5-7s7.5 2 8.5 7"/></svg>
    <svg width="26" height="22" viewBox="0 0 26 22" fill="none" stroke="#fff" stroke-width="1.5"><path d="M1 2h4l3 12h13l3-9H7"/><circle cx="10" cy="19" r="1.8"/><circle cx="19" cy="19" r="1.8"/><text x="18" y="7" font-size="7" fill="#fff" stroke="none" font-family="Jost,sans-serif">0</text></svg>
  </div>
</header>

<section class="abs hero" role="img" aria-label="Black ceramic herb grinder set with lid and pollen scraper on a dark surface"></section>
<div class="abs hero-copy">
  <h1 class="hero-title">RiverMoss Herb Grinder Set</h1>
  <p class="hero-text">RiverMoss herb grinder is made of top quality ceramic and has a matte finish which ensures that the surface of the grinder feels soft and comfortable in your palm. This unique design makes grinding herbs a smooth and efficient process alongside its great quality components.</p>
  <span class="btn-outline">SHOP NOW</span>
</div>

<div class="abs welcome">Welcome to RiverMoss Smoking Supplies</div>

<section class="abs intro" style="top:810px">
  <h2>Lorem ipsum dolor sit amet, consectetur adipiscing</h2>
  <p>Sed ut perspiciatis unde omnis iste natus error sit voluptatem accusantium doloremque laudantium, totam rem aperiam, eaque ipsa quae ab illo inventore veritatis et quasi architecto beatae vitae dicta sunt explicabo.</p>
</section>

<section class="abs products">
  <article class="card">
    <div class="photo" role="img" aria-label="Black herb grinder beside its branded box"></div>
    <h3>RiverMoss Herb Grinder Set</h3>
    <div class="rating"><svg width="90" height="16" viewBox="0 0 90 16" fill="var(--star)"><g id="st"><path d="M8 0l2.4 5 5.6.6-4.2 3.8 1.2 5.6L8 12.2 3 15l1.2-5.6L0 5.6 5.6 5z"/></g><use href="#st" x="18"/><use href="#st" x="36"/><use href="#st" x="54"/><use href="#st" x="72"/></svg>4.8 (54 Reviews)</div>
    <div class="price">$15.00</div>
  </article>
  <article class="card">
    <div class="photo" role="img" aria-label="Black UV storage stash jar 100ml beside its box"></div>
    <h3>RiverMoss UV Storage Stash Jar (100ml)</h3>
    <div class="rating"><svg width="90" height="16" viewBox="0 0 90 16" fill="var(--star)"><use href="#st"/><use href="#st" x="18"/><use href="#st" x="36"/><use href="#st" x="54"/><use href="#st" x="72"/></svg>4.8 (54 Reviews)</div>
    <div class="price">$15.00</div>
  </article>
  <article class="card">
    <div class="photo" role="img" aria-label="Black UV storage stash jar 500ml beside its box"></div>
    <h3>RiverMoss UV Storage Stash Jar (500ml)</h3>
    <div class="rating"><svg width="90" height="16" viewBox="0 0 90 16" fill="var(--star)"><use href="#st"/><use href="#st" x="18"/><use href="#st" x="36"/><use href="#st" x="54"/><use href="#st" x="72"/></svg>4.8 (54 Reviews)</div>
    <div class="price">$15.00</div>
  </article>
  <article class="card">
    <div class="photo" role="img" aria-label="Black UV storage stash jar 250ml beside its box"></div>
    <h3>RiverMoss UV Storage Stash Jar (250ml)</h3>
    <div class="rating"><svg width="90" height="16" viewBox="0 0 90 16" fill="var(--star)"><use href="#st"/><use href="#st" x="18"/><use href="#st" x="36"/><use href="#st" x="54"/><use href="#st" x="72"/></svg>4.8 (54 Reviews)</div>
    <div class="price">$15.00</div>
  </article>
</section>

<div class="abs btn-dark" style="left:528px;top:1276px;width:144px;height:47px">VIEW ALL</div>

<section class="abs stories">
  <article class="story">
    <div class="photo" role="img" aria-label="Hands opening a grinder full of herbs on a table"></div>
    <h3>FINIBUS BONORUM ET MALORUM</h3>
    <p>Lorem ipsum dolor sit amet, coiscing elit, sed do eiusmod tempor incidit ut labodolore magna aliqua. Lorem ipsum dolor sit amet, consectetur adipiscing elit</p>
  </article>
  <article class="story">
    <div class="photo" role="img" aria-label="Hand holding an open grinder with ground herbs"></div>
    <h3>FINIBUS BONORUM ET MALORUM</h3>
    <p>Lorem ipsum dolor sit amet, coiscing elit, sed do eiusmod tempor incidit ut labodolore magna aliqua. Lorem ipsum dolor sit amet, consectetur adipiscing elit</p>
  </article>
  <article class="story">
    <div class="photo" role="img" aria-label="Rolled papers lying beside a metal grinder"></div>
    <h3>FINIBUS BONORUM ET MALORUM</h3>
    <p>Lorem ipsum dolor sit amet, coiscing elit, sed do eiusmod tempor incidit ut labodolore magna aliqua. Lorem ipsum dolor sit amet, consectetur adipiscing elit</p>
  </article>
</section>

<div class="abs promo"><b>PROMOTION</b> Spend $100 and Get 5% Off <span class="btn-small">SHOP NOW</span></div>

<section class="abs feature-photo" role="img" aria-label="Man in a bathrobe holding a black stash jar in a bathroom"></section>
<div class="abs feature" style="top:2047px"><div class="dot" role="img" aria-label="Grinder magnet detail"></div><div class="pill"><h4>Strong Magnet</h4><p>Two powerful built in magnets ensure<br>contents remain contained</p></div></div>
<div class="abs feature" style="top:2187px"><div class="dot" role="img" aria-label="Grinder teeth detail"></div><div class="pill"><h4>Precise Cutting</h4><p>Knife-edged blocks guarantee a clean and<br>effortless cutting of your herbs</p></div></div>
<div class="abs feature" style="top:2327px"><div class="dot" role="img" aria-label="Steel sieve detail"></div><div class="pill"><h4>Fine Sieve</h4><p>A fine Stainless Steel Sieve allows the pollen to<br>fall into the kief compartment</p></div></div>
<div class="abs feature" style="top:2467px"><div class="dot" role="img" aria-label="Pollen compartment detail"></div><div class="pill"><h4>Pollen Carriage</h4><p>the smooth edge design of the lower<br>compartment makes it easier to remove herbs</p></div></div>

<section class="abs intro" style="top:2768px">
  <h2>Lorem ipsum dolor sit amet, consectetur adipiscing</h2>
  <p>Sed ut perspiciatis unde omnis iste natus error sit voluptatem accusantium doloremque laudantium, totam rem aperiam, eaque ipsa quae ab illo inventore veritatis et quasi architecto beatae vitae dicta sunt explicabo.</p>
</section>

<div class="photo duo duo-left" role="img" aria-label="Open gift box with grinder, lid and accessories"></div>
<div class="photo duo duo-right" role="img" aria-label="Hand placing a black pouch in a car interior"></div>

<article class="abs offer" style="left:79px">
  <h3>Lorem ipsum dolor set, consectetur adipiscing elit, sed</h3>
  <p>Lorem ipsum dolor sit amet, coctetur adipiscing elit, sed do eiusmod tempor incididunt ut labore et dolore magna aliqua. Quis ipsum suspendisse ultrices gravida.</p>
  <div class="btn-dark">SHOP NOW</div>
</article>
<div class="offer-photo" style="left:367px;width:223px" role="img" aria-label="Black grinder in front of its box"></div>

<article class="abs offer" style="left:627px">
  <h3>Lorem ipsum dolor set, consectetur adipiscing elit, sed</h3>
  <p>Lorem ipsum dolor sit amet, coctetur adipiscing elit, sed do eiusmod tempor incididunt ut labore et dolore magna aliqua. Quis ipsum suspendisse ultrices gravida.</p>
  <div class="btn-dark">SHOP NOW</div>
</article>
<div class="offer-photo" style="left:915px;width:240px" role="img" aria-label="Grinder set with box and small accessories"></div>

<section class="abs signup">
  <h2>SIGN UP AND SAVE</h2>
  <p>Subscribe to get special offers, free giveaways, and once-in-a-lifetime deals.</p>
  <div class="signup-form"><span>Enter your email</span><b>SUBSCRIBE</b></div>
</section>

<footer class="abs footer">
  <div class="brand">RiverMoss<small>SMOKING SUPPLIES</small></div>
  <div class="socials"><i></i><i></i><i></i></div>
  <div class="fcol" style="left:366px"><h5>SUPPORT</h5><ul><li>Search</li><li>FAQ</li><li>Contact Us</li><li>Wholesale</li></ul></div>
  <div class="fcol" style="left:523px"><h5>INFO</h5><ul><li>Shipping &amp; Delivery</li><li>Terms of Service</li><li>Privacy Policy</li><li>Return and Refund Policy</li><li>Price Promise Terms &amp; Conditions</li></ul></div>
  <div class="fcol" style="left:823px"><h5>SIGN UP AND SAVE</h5><p>Subscribe to get special offers, free giveaways, and once-in-a-lifetime deals.</p>
    <div class="fmail">Enter your email<svg width="16" height="16" viewBox="0 0 16 16" fill="#fff"><path d="M1 7.5 15 1l-5 14-2.5-5.5z"/></svg></div>
  </div>
  <div class="frule"></div>
  <div class="copy">© 2021 RiverMoss Smoking Supplies. All Rights Reserved</div>
  <div class="cards"><i></i><i></i><i></i><i></i><i></i></div>
</footer>

</body>
</html>
```